Plakat-Design für Blasmusik Konzert
Zielgruppe
Wir - die Tordinger Blasmusik e.V. - sind auf der Suche nach:
einem Plakatdesign in A1 & A2 und passendem
Ticket-Design DIN lang quer inkl. Perforierung und 2x Nummerierung
für unser Konzert 2019 mit dem Motto:
'NIGHTS OF WONDER'.
Das Konzert wird einen weiten Rahmen von Henrik Dallmann und Brisko hin zu Bernd Falkenrath und Tom Kellin. Auch Titel aus dem Bereich Filmmusik wird es geben. Also ein bunter Abend mit Gesang und Showlicht.
Wir freuen uns auf eure Ideen!!!
Impressionen: www.tordinger-blasmusik.de
Aufgabenstellung
Stichworte: Bunt, Modern, Edel
Facts:
Samstag 05.10.2019 Beginn 19:00
Festsaal am Lindenhof, Tordingen am Bach
Eintritt 15€, Kinder bis einschließlich 8 Jahre Eintritt frei.
'Mehr Informationen unter www.tordinger-blasmusik.de und auf Plaudernet'
Für Ticket: Einlass ab 18:30 Uhr. Freie Platzwahl.
Irgendwo auf dem Plakat muss Platz für die dezente Nennung von 2-3 Sponsoren vorgesehen werden. Diese würden wir nachträglich einfügen. Auch ein 'Find us on Plaudernet'-Icon wäre cool.
Die Druckdateien (CMYK) sind mit entsprechendem Beschnitt gemäß Vorgabe von 'flott-gedruckt-jetzt' anzulegen und als Vector-Datei sowie PDF zu übergeben.

```html
<!DOCTYPE html>
<html lang="de">
<head>
<meta charset="utf-8">
<title>Nights of Wonder – Konzert 2019</title>
<link href="https://fonts.googleapis.com/css2?family=Fira+Sans:ital,wght@0,400;0,500;0,600;1,500&family=Great+Vibes&display=swap" rel="stylesheet">
<style>
  :root {
    --backdrop: #d9d9d9;
    --poster: #5b5b5b;
    --white: #ffffff;
    --band: #6c2a80;
    --badge: #c62fd3;
    --rule: #bdbdbd;
    --sponsor-text: #222222;
  }
  * { margin: 0; padding: 0; box-sizing: border-box; }
  html, body { width: 1200px; height: 1200px; overflow: hidden; background: var(--backdrop); }
  body { font-family: "Fira Sans", sans-serif; color: var(--white); }

  .poster {
    position: absolute; left: 205px; top: 40px;
    width: 790px; height: 1120px;
    background: var(--poster); overflow: hidden;
  }
  .club-name {
    position: absolute; left: 29px; top: 30px;
    font-size: 36px; font-weight: 600; line-height: 1.1;
  }
  .event-facts { position: absolute; right: 16px; top: 12px; text-align: right; }
  .event-date, .event-time { font-size: 42px; font-weight: 500; line-height: 48px; }
  .event-rule { width: 277px; height: 2px; background: var(--rule); margin: 6px 0 10px auto; }
  .event-venue { font-size: 22px; line-height: 28px; }

  .splash-art {
    position: absolute; left: 21px; top: 154px; width: 747px; height: 746px;
    background:
      radial-gradient(circle at 30% 35%, rgba(60,150,230,.85), transparent 35%),
      radial-gradient(circle at 62% 30%, rgba(255,200,40,.8), transparent 30%),
      radial-gradient(circle at 48% 22%, rgba(240,70,170,.85), transparent 32%),
      radial-gradient(circle at 70% 70%, rgba(230,60,200,.85), transparent 35%),
      radial-gradient(circle at 35% 72%, rgba(90,110,230,.85), transparent 35%),
      radial-gradient(circle at 80% 45%, rgba(240,90,60,.75), transparent 28%),
      radial-gradient(circle at 50% 50%, rgba(140,80,200,.6), transparent 60%);
    border-radius: 50%;
  }
  .title {
    position: absolute; left: 0; width: 100%; text-align: center;
    font-family: "Great Vibes", cursive; font-weight: 400; line-height: 1;
    text-shadow: 0 2px 8px rgba(0,0,0,.25);
  }
  .title-line-1 { top: 270px; font-size: 220px; }
  .title-line-2 { top: 500px; font-size: 190px; }
  .subtitle {
    position: absolute; left: 0; width: 100%; top: 704px; text-align: center;
    font-size: 48px; font-weight: 500;
  }
  .price-badge {
    position: absolute; left: 610px; top: 744px; width: 152px; height: 152px;
    border-radius: 50%; background: var(--badge);
    display: flex; flex-direction: column; align-items: center; justify-content: center;
    font-size: 32px; font-weight: 500; line-height: 40px;
  }
  .lineup { position: absolute; left: 0; width: 100%; top: 918px; text-align: center; font-size: 25px; font-weight: 500; line-height: 32px; }
  .footnote { position: absolute; left: 0; width: 100%; top: 997px; text-align: center; font-size: 14px; }

  .info-band {
    position: absolute; left: 0; top: 1022px; width: 100%; height: 98px; background: var(--band);
  }
  .info-label { position: absolute; left: 12px; top: 12px; font-size: 13px; }
  .info-link { position: absolute; left: 12px; font-size: 17px; font-weight: 500; white-space: nowrap; }
  .info-link.social { top: 39px; display: flex; align-items: center; gap: 6px; }
  .info-link.web { top: 64px; }
  .social-mark { width: 13px; height: 13px; background: var(--white); display: inline-block; }
  .sponsor {
    position: absolute; top: 12px; width: 125px; height: 74px; background: var(--white);
    display: flex; align-items: center; justify-content: center;
    color: var(--sponsor-text); font-size: 18px; font-weight: 600;
  }
  .sponsor-1 { left: 386px; }
  .sponsor-2 { left: 523px; }
  .sponsor-3 { left: 659px; }
</style>
</head>
<body>
<main class="poster">
  <div class="club-name">Tordinger<br>Blasmusik e.V.</div>

  <div class="event-facts">
    <div class="event-date">Sa. 05.10.2019</div>
    <div class="event-time">Beginn: 19.00</div>
    <div class="event-rule"></div>
    <div class="event-venue">Festsaal am Lindenhof,<br>Tordingen am Bach</div>
  </div>

  <div class="splash-art" role="img" aria-label="Farbexplosion in Pink, Blau, Gelb und Violett mit Silhouetten von Blechblasinstrumenten"></div>

  <h1 class="title title-line-1">Nights</h1>
  <div class="title title-line-2">of Wonder</div>
  <div class="subtitle">Konzert 2019</div>

  <div class="price-badge"><span>Eintritt</span><span>15€*</span></div>

  <p class="lineup">Henrik Dallmann…Brisko…Bernd Falkenrath…Tom Kellin<br>Bunter Abend mit Gesang und Showlicht</p>
  <p class="footnote">*Kinder bis einschließlich 8 Jahre Eintritt frei. Für Ticket: Einlass ab 18:30 Uhr. Freie Platzwahl.</p>

  <footer class="info-band">
    <div class="info-label">Mehr Informationen :</div>
    <div class="info-link social"><span class="social-mark"></span>plaudernet.com/Tordinger-Blasmusik-eV</div>
    <div class="info-link web">www.tordinger-blasmusik.de</div>
    <div class="sponsor sponsor-1">Saitenhaus</div>
    <div class="sponsor sponsor-2">Trommelwerk</div>
    <div class="sponsor sponsor-3">Klangreich</div>
  </footer>
</main>
</body>
</html>
```